Pull-Up Banner for creating escape room themed engaging learning experiences

Our research group create engaging learning experiences aimed at the following markets: Primary school, secondary school, tertiary and corporate training. We want learning to be fun, but also deep - where participants will need to think deeply and apply themselves to solve problems as a team.
We are the inventors of the open source escape room decoder box and want to engage students in learning in a fun way which maximizes teamwork. We are also keen to be contracted to design custom escape room learning experiences for corporate entities to engage their staff and have them working together as a team.

```html
<!DOCTYPE html>
<html lang="en">
<head>
<meta charset="utf-8">
<title>Pull-Up Banner – The Key to Maximizing Teamwork</title>
<link rel="stylesheet" href="https://fonts.googleapis.com/css2?family=Archivo+Black&family=Audiowide&display=swap">
<style>
  :root {
    --page-bg: #eeeeee;
    --banner-white: #ffffff;
    --brand-orange: #f28a1e;
    --brand-orange-deep: #ee6a1f;
    --brand-blue: #2f8fd6;
    --ink: #111111;
    --ink-grey: #3a3a3a;
    --photo-dark: #2b2b2e;
    --photo-warm: #8a6e5a;
    --photo-light: #cfd3d6;
  }
  * { box-sizing: border-box; margin: 0; padding: 0; }
  html, body { width: 1200px; height: 900px; overflow: hidden; }
  body {
    position: relative;
    background: radial-gradient(ellipse at 50% 40%, #fafafa 0%, var(--page-bg) 70%);
    font-family: "Archivo Black", Arial, sans-serif;
  }
  .banner {
    position: absolute;
    top: 85px;
    width: 293px;
    height: 693px;
    background: var(--banner-white);
    overflow: hidden;
    box-shadow: 0 2px 6px rgba(0,0,0,.18);
  }
  .banner--orange { left: 257px; }
  .banner--white { left: 651px; }

  .header-band {
    position: absolute; left: 0; top: 0; width: 100%; height: 192px;
    background: linear-gradient(180deg, var(--brand-orange-deep) 0%, var(--brand-orange) 100%);
  }
  .ribbon { position: absolute; left: 102px; top: 0; width: 89px; height: 77px; }

  .headline { position: absolute; left: 0; width: 100%; text-align: center; }
  .headline__lead { font-size: 20px; letter-spacing: .5px; line-height: 1; }
  .headline__main {
    font-family: "Audiowide", "Arial Black", sans-serif;
    font-style: italic;
    font-size: 34px;
    line-height: 30px;
    text-transform: uppercase;
    margin-top: 6px;
    letter-spacing: 1px;
  }
  .banner--orange .headline { top: 52px; color: #fff; }
  .banner--white .headline { top: 98px; }
  .banner--white .headline__lead { color: var(--ink-grey); font-size: 22px; }
  .banner--white .headline__main { color: var(--brand-blue); }

  .photo { position: absolute; }
  .photo--hero {
    left: 0; width: 100%; height: 143px;
    background: linear-gradient(100deg, var(--photo-light) 0%, var(--photo-warm) 45%, var(--photo-dark) 100%);
  }
  .photo--tile { width: 138px; height: 69px; }
  .photo--a { background: linear-gradient(120deg, #6b6058, #b9a38e 60%, #3c3a3a); }
  .photo--b { background: linear-gradient(120deg, #1f2230, #4b4450 55%, #8a7a6a); }
  .photo--c { background: linear-gradient(120deg, #3e6b3a, #7d5a4a 55%, #c9b7a5); }
  .photo--d { background: linear-gradient(120deg, #120f10, #3a1414 50%, #8a8d92); }

  .markets {
    position: absolute;
    list-style: none;
    text-align: right;
    color: var(--ink);
    letter-spacing: .2px;
    white-space: nowrap;
  }
  .banner--orange .markets { right: 34px; top: 532px; font-size: 9.5px; line-height: 16px; }
  .banner--white .markets { right: 34px; top: 546px; font-size: 8.5px; line-height: 13.5px; }

  .brand__mark {
    position: absolute;
    width: 80px; height: 80px; border-radius: 50%;
    background: var(--brand-orange);
  }
  .banner--orange .brand__mark { left: 22px; top: 565px; }
  .banner--white .brand__mark { left: 22px; top: 568px; }

  .brand__name {
    position: absolute;
    font-size: 14px; line-height: 15px;
    color: var(--brand-blue);
    text-transform: uppercase;
    letter-spacing: .3px;
    white-space: nowrap;
  }
  .banner--orange .brand__name { left: 116px; top: 611px; }
  .banner--white .brand__name { left: 117px; top: 614px; }

  .social {
    position: absolute; right: 41px; top: 654px;
    display: flex; gap: 5px; list-style: none;
  }
  .social__dot { width: 13px; height: 13px; border-radius: 50%; background: var(--ink); }
</style>
</head>
<body>

<section class="banner banner--orange" aria-label="Banner option with orange header">
  <div class="header-band"></div>
  <h1 class="headline">
    <div class="headline__lead">THE KEY TO</div>
    <div class="headline__main">Maximizing<br>Teamwork</div>
  </h1>
  <div class="photo photo--hero" style="top:192px" role="img" aria-label="Photo of a team working together around a table on a puzzle"></div>
  <div class="photo photo--tile photo--a" style="left:0;top:345px" role="img" aria-label="Photo of three adults solving a puzzle box"></div>
  <div class="photo photo--tile photo--b" style="left:155px;top:345px" role="img" aria-label="Photo of three people examining clues"></div>
  <div class="photo photo--tile photo--c" style="left:0;top:430px" role="img" aria-label="Photo of students leaning over a worksheet"></div>
  <div class="photo photo--tile photo--d" style="left:155px;top:430px" role="img" aria-label="Photo of hands using a decoder box keypad"></div>
  <ul class="markets">
    <li>PRIMARY SCHOOL</li>
    <li>SECONDARY SCHOOL</li>
    <li>TERTIARY SCHOOL</li>
    <li>CORPORATE TRAINING</li>
  </ul>
  <span class="brand__mark"></span>
  <span class="brand__name">Puzzle Lock<br>Learning</span>
  <ul class="social" aria-label="Social links">
    <li class="social__dot"></li><li class="social__dot"></li><li class="social__dot"></li>
  </ul>
</section>

<section class="banner banner--white" aria-label="Banner option with white header">
  <svg class="ribbon" viewBox="0 0 89 77" aria-hidden="true">
    <polygon points="0,0 89,0 89,77 44.5,55 0,77" fill="var(--brand-orange)"/>
  </svg>
  <h1 class="headline">
    <div class="headline__lead">THE KEY TO</div>
    <div class="headline__main">Maximizing<br>Teamwork</div>
  </h1>
  <div class="photo photo--hero" style="top:220px;height:147px" role="img" aria-label="Photo of a team working together around a table on a puzzle"></div>
  <div class="photo photo--tile photo--a" style="left:0;top:380px" role="img" aria-label="Photo of three adults solving a puzzle box"></div>
  <div class="photo photo--tile photo--b" style="left:154px;top:380px;width:139px" role="img" aria-label="Photo of three people examining clues"></div>
  <div class="photo photo--tile photo--c" style="left:0;top:463px" role="img" aria-label="Photo of students leaning over a worksheet"></div>
  <div class="photo photo--tile photo--d" style="left:154px;top:463px;width:139px" role="img" aria-label="Photo of hands using a decoder box keypad"></div>
  <ul class="markets">
    <li>PRIMARY SCHOOL</li>
    <li>SECONDARY SCHOOL</li>
    <li>TERTIARY SCHOOL</li>
    <li>CORPORATE TRAINING</li>
  </ul>
  <span class="brand__mark"></span>
  <span class="brand__name">Puzzle Lock<br>Learning</span>
  <ul class="social" aria-label="Social links">
    <li class="social__dot"></li><li class="social__dot"></li><li class="social__dot"></li>
  </ul>
</section>

</body>
</html>
```